TIDAL PUFF- New packaging design

Create new packaging design for Tidal Puff.
We are looking to update our packaging design onto our new box.
Designer must be creative and produce all the required elements as needed.
Designer will create new packaging layout, change color scheme of logo as needed, create new background design, etc.
Please use Example designs as reference. These are the companies/ designs we want to resemble.
Design die-line and guideline files are attached.
FRONT DESIGN OF BOX:
Attached to the files is our OLD PACKAGING file that we currently use. Most of the design will be transferred over with the addition of the CA Instituted THC label (file attached)
-Tidal Puff logo
-THC label
-"500mg"
-"Net WT .5g"
BACK DESIGN OF BOX:
Attached to the files is BACK EXAMPLE file. We need most of the info in the back transferred over to the new box dieline.
-Directions:
1. Remove vaporizer cartridge from package and remove rubber stoppers.
2. Screw Cartridge clockwise onto any 510 threaded battery of your choice.
-Store at room temperature.
Direct sunlight and excessive heat may cause the cartridge to leak.
-"GOVERNMENT WARNING: THIS PRODUCT CONTAINS CANNABIS, A SCHEDULE I CONTROLLED SUBSTANCE. KEEP OUT OF REACH OF CHILDREN AND ANIMALS. CANNABIS PRODUCTS MAY ONLY BE POSSESSED OR CONSUMED BY PERSONS 21 YEARS OF AGE OR OLDER UNLESS THE PERSON IS A QUALIFIED PATIENT. THE INTOXICATING EFFECTS OF CANNABIS PRODUCTS MAY BE DELAYED UP TO TWO HOURS. CANNABIS USE WHILE PREGNANT OR BREASTFEEDING MAY BE HARMFUL. CONSUMPTION OF CANNABIS PRODUCTS IMPAIRS YOUR ABILITY TO DRIVE AND OPERATE MACHINERY. PLEASE USE EXTREME CAUTION."
INNER TRAY OF BOX:
(will be designed after outer carton of box is finished)

```html
<!DOCTYPE html>
<html lang="en">
<head>
<meta charset="utf-8">
<title>Tidal Puff – Cartridge Carton Dieline</title>
<link rel="stylesheet" href="https://fonts.googleapis.com/css2?family=Open+Sans:wght@400;600;700;800&display=swap">
<style>
  :root {
    --canvas: #ffffff;
    --carton: #2a2a3c;
    --pattern: #3b3b52;
    --lime: #8dc63f;
    --pink: #f092bf;
    --white: #ffffff;
    --guide-red: #e0262c;
    --cut-line: #111111;
    --ink-dark: #2a2a3c;
  }
  html, body {
    margin: 0;
    padding: 0;
    width: 1200px;
    height: 800px;
    overflow: hidden;
    background: var(--canvas);
  }
  .carton-dieline {
    display: block;
    width: 1200px;
    height: 800px;
    font-family: "Open Sans", sans-serif;
  }
  .carton-body { fill: var(--carton); }
  .guide-line { stroke: var(--guide-red); stroke-width: 1.3; fill: none; }
  .fold-line { stroke: var(--cut-line); stroke-width: 1.2; fill: none; }
  .band-lime { fill: var(--lime); }
  .band-white { fill: var(--white); }
  .band-pink { fill: var(--pink); }
  .band-dark { fill: var(--carton); }
  .brand-name { fill: var(--lime); font-weight: 800; }
  .copy { fill: var(--white); }
  .copy-bold { font-weight: 700; }
  .warning { fill: var(--white); font-size: 8.6px; font-weight: 600; }
  .potency { fill: var(--ink-dark); font-weight: 700; }
  .badge-shape { fill: #1c1c2a; stroke: #3d3d52; stroke-width: 1; }
  .mark-placeholder { fill: var(--pink); }
</style>
</head>
<body>
<svg class="carton-dieline" viewBox="0 0 1500 1000" xmlns="http://www.w3.org/2000/svg">

  <!-- carton silhouette -->
  <g class="carton-body" role="img" aria-label="Dark navy carton with a repeating tonal brand-symbol pattern">
    <rect x="100" y="120" width="140" height="170" rx="30"/>
    <rect x="100" y="230" width="325" height="560"/>
    <rect x="425" y="236" width="121" height="560"/>
    <path d="M546 258 L546 170 L600 88 L740 88 L740 258 Z"/>
    <rect x="740" y="118" width="125" height="150" rx="28"/>
    <rect x="546" y="240" width="426" height="540"/>
    <rect x="865" y="152" width="130" height="120"/>
    <rect x="995" y="245" width="55" height="30"/>
    <rect x="1050" y="152" width="162" height="120"/>
    <path d="M972 245 L1212 245 L1360 300 Q1405 310 1405 360 L1405 740 Q1405 785 1360 785 L972 785 Z"/>
    <rect x="100" y="760" width="325" height="152" rx="40"/>
    <rect x="425" y="760" width="121" height="112"/>
    <rect x="546" y="760" width="305" height="152" rx="40"/>
    <rect x="851" y="760" width="144" height="135"/>
  </g>

  <!-- fold and tuck lines -->
  <g class="fold-line">
    <path d="M120 258 L128 150 Q130 143 138 143 L205 143 Q212 143 214 150 L222 258"/>
    <path d="M120 772 L128 880 Q130 888 140 888 L405 888 Q415 888 417 880 L420 772"/>
    <path d="M428 772 L428 870 L544 870 L544 772"/>
    <path d="M550 772 L556 880 Q558 888 568 888 L830 888 Q840 888 842 880 L846 772"/>
    <path d="M760 258 L766 150 Q768 140 778 140 L840 140 Q850 140 852 150 L858 258"/>
    <path d="M870 258 L872 175 L970 175 L972 258"/>
    <path d="M852 772 L856 870 L990 870"/>
    <path d="M975 262 L1072 262 L1072 772 L975 772"/>
    <path d="M945 580 A45 45 0 1 0 945 665" />
  </g>

  <!-- colour bands -->
  <rect class="band-lime" x="100" y="617" width="972" height="34"/>
  <rect class="band-white" x="100" y="657" width="972" height="31"/>
  <rect class="band-pink" x="100" y="697" width="972" height="10"/>

  <!-- panel guides -->
  <g class="guide-line">
    <line x1="120" y1="258" x2="972" y2="258"/>
    <line x1="120" y1="772" x2="972" y2="772"/>
    <line x1="425" y1="258" x2="425" y2="772"/>
    <line x1="546" y1="258" x2="546" y2="772"/>
    <line x1="851" y1="258" x2="851" y2="772"/>
    <line x1="972" y1="258" x2="972" y2="772"/>
  </g>

  <!-- FRONT PANEL -->
  <g class="front-panel">
    <rect class="badge-shape" x="132" y="293" width="50" height="50" rx="3" role="img" aria-label="State THC warning badge"/>
    <text class="brand-name" x="270" y="462" font-size="50" text-anchor="middle">Tidal Puff</text>
    <text class="potency" x="140" y="644" font-size="28">500<tspan font-weight="400" font-size="24">mg</tspan></text>
    <text class="potency" x="404" y="681" font-size="17" text-anchor="end">Net WT <tspan font-size="24">.5g</tspan></text>
  </g>

  <!-- LEFT SIDE PANEL -->
  <g class="side-panel">
    <text class="brand-name" transform="translate(505 585) rotate(-90)" font-size="46">Tidal Puff</text>
    <text class="copy copy-bold" font-size="10.5" text-anchor="middle">
      <tspan x="485" y="720">Lab Tested</tspan>
      <tspan x="485" y="734">Contaminate &amp;</tspan>
      <tspan x="485" y="748">Solvent Free</tspan>
      <tspan x="485" y="761">Extract</tspan>
    </text>
  </g>

  <!-- BACK PANEL -->
  <g class="back-panel">
    <text class="copy" font-size="12.5">
      <tspan x="556" y="283" font-weight="700">Directions:</tspan>
      <tspan x="556" y="296"><tspan font-weight="700">1.</tspan> Remove vaporizer cartridge from package and</tspan>
      <tspan x="556" y="308">remove rubber stoppers.</tspan>
      <tspan x="556" y="320"><tspan font-weight="700">2.</tspan> Screw Cartridge clockwise onto any 510</tspan>
      <tspan x="556" y="332">threaded battery of your choice.</tspan>
    </text>
    <circle class="mark-placeholder" cx="700" cy="412" r="46" role="img" aria-label="Brand emblem area"/>
    <text class="warning" text-anchor="middle">
      <tspan x="698" y="510">"GOVERNMENT WARNING: THIS PRODUCT CONTAINS CANNA-</tspan>
      <tspan x="698" y="520.5">BIS, A SCHEDULE I CONTROLLED SUBSTANCE. KEEP OUT OF</tspan>
      <tspan x="698" y="531">REACH OF CHILDREN AND ANIMALS. CANNABIS PRODUCTS MAY</tspan>
      <tspan x="698" y="541.5">ONLY BE POSSESSED OR CONSUMED BY PERSONS 21 YEARS OF</tspan>
      <tspan x="698" y="552">AGE OR OLDER UNLESS THE PERSON IS A QUALIFIED PATIENT.</tspan>
      <tspan x="698" y="562.5">THE INTOXICATING EFFECTS OF CANNABIS PRODUCTS MAY BE</tspan>
      <tspan x="698" y="573">DELAYED UP TO TWO HOURS. CANNABIS USE WHILE PREGNANT</tspan>
      <tspan x="698" y="583.5">OR BREASTFEEDING MAY BE HARMFUL. CONSUMPTION OF</tspan>
      <tspan x="698" y="594">CANNABIS PRODUCTS IMPAIRS YOUR ABILITY TO DRIVE AND</tspan>
      <tspan x="698" y="604.5">OPERATE MACHINERY. PLEASE USE EXTREME CAUTION."</tspan>
    </text>
    <text class="copy" font-size="12.5">
      <tspan x="563" y="721" font-weight="700">Store at room temperature.</tspan>
      <tspan x="563" y="735">Direct sunlight and excessive heat may</tspan>
      <tspan x="563" y="749">cause the cartridge to leak.</tspan>
    </text>
  </g>

  <!-- TOP TUCK -->
  <circle class="mark-placeholder" cx="804" cy="200" r="26" role="img" aria-label="Brand emblem area"/>

  <!-- RIGHT SIDE PANEL -->
  <text class="brand-name" transform="translate(930 548) rotate(-90)" font-size="46">Tidal Puff</text>

</svg>
</body>
</html>
```